Design a Website Mockup for Athletics Training Site - repost

We need an overall site design along with several specific elements for an athletic teaching resources site. In addition to the website design we also need a logo that will be used for all online and offline materials. I have attached several documents to give the designer some idea of what we are looking for in terms content and structure. Need to have the site designed to utilize responsive design to format site for smaller phone, tablet to larger desktop screens. This will require that multiple mockups be provided for each template. Please provide all final products as Adobe Photoshop layered image files that are well organized and will allow individual elements to be separated and used in the final website.

```html
<!DOCTYPE html>
<html lang="en">
<head>
<meta charset="utf-8">
<title>Sitename – Home</title>
<link rel="stylesheet" href="https://fonts.googleapis.com/css2?family=Ubuntu:wght@400;500;700&family=Arimo:wght@400;700&display=swap">
<style>
:root{
  --page-bg:#d8dce2;
  --panel:#eef0f3;
  --white:#f8f9fa;
  --blue:#4f76a8;
  --blue-dark:#34598a;
  --blue-light:#6d91bf;
  --link:#4a7ab8;
  --ink:#3b3e43;
  --ink-soft:#5e6168;
  --gray-bar:#bfc2c7;
  --gray-box:#d3d5d8;
  --frame:#b5b8bd;
  --dark-label:#2a2b2e;
  --footer:#c8ccd2;
  --footer-bottom:#5a5b5e;
}
*{box-sizing:border-box;margin:0;padding:0}
html,body{width:896px;height:1200px;overflow:hidden}
body{position:relative;background:var(--page-bg);font-family:"Arimo",Arial,sans-serif;color:var(--ink-soft);font-size:9px;line-height:1.45}
.abs{position:absolute}
.heading{font-family:"Ubuntu",Arial,sans-serif}

/* header */
.top-band{left:0;top:0;width:896px;height:44px;background:linear-gradient(#6a8cb9,#3f6797)}
.nav-band{left:0;top:44px;width:896px;height:34px;background:linear-gradient(#b9bdc3,#8f949b);border-bottom:1px solid #7c8188}
.logo-ring{left:158px;top:4px;width:68px;height:68px;border-radius:50%;background:#b7bcc3;border:3px solid #9aa0a8;display:flex;align-items:center;justify-content:center}
.logo-core{width:44px;height:44px;border-radius:50%;background:#e9ebee;color:#333;font-size:7px;text-align:center;display:flex;align-items:center;justify-content:center;line-height:1.1}
.site-name{left:236px;top:8px;font-family:"Ubuntu",sans-serif;font-size:26px;color:#eef2f7;letter-spacing:1px;font-weight:400}
.top-menu{left:506px;top:21px;display:flex;border:1px solid #2b4a72;background:linear-gradient(#4a6f9f,#35598a)}
.top-menu span{color:#fff;font-weight:700;font-size:9px;padding:5px 11px;border-right:1px solid #2b4a72}
.top-menu span:last-child{border-right:0}
.main-nav{left:238px;top:52px;display:flex;gap:0}
.main-nav span{font-size:10px;color:#2e3136;padding:6px 12px 8px}
.main-nav .active{background:linear-gradient(#a5aab1,#878c94);color:#fff;border-bottom:3px solid var(--blue-light)}

/* social tab */
.social{left:874px;top:100px;width:22px}
.social i{display:block;height:24px;margin-bottom:2px;background:#6e7377;border:1px solid #555}
.social i:nth-child(1){background:#6d8aa0}
.social i:nth-child(2){background:#5b6f8c}
.social i:nth-child(3){background:#8c6b62}
.social i:nth-child(4){background:#8a7f5a}

/* main panel */
.panel{left:157px;top:78px;width:585px;height:865px;background:var(--panel);border-radius:0 0 4px 4px;box-shadow:0 1px 3px rgba(0,0,0,.25)}
.hero{left:157px;top:80px;width:585px;height:246px;background:radial-gradient(ellipse at 65% 45%,#4a4540 0%,#1a1a1a 45%,#050505 80%),#000;}
.hero::after{content:"";position:absolute;left:0;right:0;bottom:0;height:50px;background:linear-gradient(transparent,#c9ced6)}
.hero-title{left:170px;top:191px;height:40px;padding:0 10px;background:rgba(0,0,0,.82);color:#fff;font-size:23px;line-height:40px;font-weight:500}
.hero-text{left:170px;top:240px;width:309px;height:68px;padding:8px 9px;background:rgba(0,0,0,.82);color:#f0f0f0;font-size:8.6px;line-height:1.5}
.slide-num{left:730px;width:24px;height:22px;background:#111;color:#fff;font-size:9px;font-weight:700;text-align:center;line-height:22px}
.slide-num.active{left:720px;width:34px;background:var(--blue-light)}

/* articles */
.card{background:#dcdee1;border:1px solid var(--frame)}
.photo{background:linear-gradient(#6b7380,#c9ced6)}
.label{background:var(--dark-label);color:#fff;font-family:"Ubuntu",sans-serif;font-size:14px;padding:0 6px;line-height:28px;height:28px;border:1px solid #555}
.card-body{background:var(--white)}
.card-title{font-size:12.5px;color:#3a3d42;font-weight:500}
.bullets{list-style:none}
.bullets li{padding-left:12px;position:relative;margin-bottom:6px}
.bullets li::before{content:"";position:absolute;left:2px;top:4px;width:4px;height:4px;border-radius:50%;background:var(--link)}
.bullets b{color:var(--link)}
.share{left:508px;top:330px;width:32px;height:86px;background:#e1e3e6;border-left:1px solid #c8cbcf;text-align:center;font-size:6px;color:#777;padding-top:3px}
.share i{display:block;width:16px;height:16px;margin:6px auto 0;background:#b9bdc2;border-radius:2px}
.dot-list{display:grid;grid-template-columns:172px 172px;row-gap:9px}
.dot-list span{padding-left:16px;position:relative;font-size:8.5px}
.dot-list span::before{content:"";position:absolute;left:2px;top:2px;width:7px;height:7px;border-radius:50%;background:#9fa3a9}
.btn{background:var(--blue);color:#fff;font-size:6.5px;font-weight:700;padding:0 6px;line-height:16px;height:16px;border:1px solid var(--blue-dark)}

/* sidebar */
.search{left:552px;top:327px;width:178px;height:81px;background:linear-gradient(#6b8fbe,#4c74a7);color:#fff;padding:10px 9px}
.search h3{font-family:"Ubuntu",sans-serif;font-weight:400;font-size:10.5px}
.search .field{margin-top:10px;height:19px;background:#557cad;border:1px solid #3c618f;color:#dce5f1;font-size:8px;padding:3px 4px}
.search .opts{margin-top:6px;font-size:8px;display:flex;gap:12px}
.search .opts span::before{content:"";display:inline-block;width:5px;height:5px;border-radius:50%;background:#c7d4e6;margin-right:5px}
.info-box{left:552px;top:418px;width:178px;height:124px;background:#e4e6e9;border:2px solid #c9ccd0;padding:10px 8px}
.info-box h3{font-family:"Ubuntu",sans-serif;font-size:9.5px;font-weight:500;color:#4a4d52;margin-bottom:10px}
.info-box p{font-size:8px;margin-bottom:8px}
.tabs{left:552px;top:562px;width:178px;height:24px;border-bottom:4px solid var(--gray-bar);display:flex}
.tabs span{font-size:8.5px;color:#333;padding:5px 9px;font-family:"Ubuntu",sans-serif}
.tabs .active{background:#c7cbd0;border-bottom:2px solid var(--blue-light)}
.thumb{border:3px solid #c3c6cb;background:linear-gradient(#9c8a77,#e2d7c9)}
.side-text{font-size:8px;width:118px}

/* ticker */
.ticker{left:170px;top:739px;width:560px;height:25px;background:#dfe1e4;border:1px solid #c3c6ca;display:flex;align-items:center;padding-left:5px;font-size:8.5px}
.ticker b{color:#333;margin-right:8px}
.ticker .arrows{position:absolute;right:4px;top:5px;display:flex;gap:3px}
.ticker .arrows i{width:13px;height:13px;border-radius:50%;background:var(--link);display:block}

/* three columns */
.col-head{font-family:"Ubuntu",sans-serif;font-size:9px;color:#45484d}
.col-bar{height:7px;background:var(--gray-bar)}
.frame{border:3px solid #bdc0c4;background:#e7e9ec}
.caption{background:rgba(0,0,0,.85);color:#fff;font-size:8px;padding:3px 7px}
.slider{left:560px;top:822px;width:162px;height:92px;background:#dfe1e4;border:1px solid #c4c7cb}
.slider h4{background:linear-gradient(#5f84b4,#466c9d);color:#fff;font-size:9px;padding:3px 7px;height:18px}
.slider p{padding:6px 7px;font-size:8px}

/* footer */
.footer{left:0;top:952px;width:896px;height:224px;background:var(--footer);border-top:1px solid #b4b8be}
.footer-bottom{left:0;top:1176px;width:896px;height:24px;background:var(--footer-bottom)}
.to-top{left:441px;top:1190px;width:14px;height:10px;background:#2d2e30;border-radius:2px 2px 0 0}
.f-head{font-family:"Ubuntu",sans-serif;font-size:8.5px;color:#44474c}
.f-list{list-style:none;font-size:8px}
.f-list li{padding-left:12px;position:relative;margin-bottom:4px}
.f-list li::before{content:"";position:absolute;left:0;top:3px;width:7px;height:7px;border-radius:50%;background:#9a9ea5}
.f-list b{color:var(--link);font-size:9px;display:block}
.f-text{font-size:8px}
.contact-row{display:flex;gap:14px;font-size:9.5px;color:#3d4045}
.contact-row a{color:var(--link);text-decoration:none}
</style>
</head>
<body>

<header>
  <div class="abs top-band"></div>
  <div class="abs nav-band"></div>
  <div class="abs logo-ring"><div class="logo-core">logo<br>space</div></div>
  <div class="abs site-name">SITENAME</div>
  <nav class="abs top-menu"><span>Nulla</span><span>turpis</span><span>hendrerit</span><span>convallis</span></nav>
  <nav class="abs main-nav"><span class="active">Home</span><span>Curabitur ▾</span></nav>
</header>

<div class="abs social" aria-label="Social links"><i></i><i></i><i></i><i></i></div>

<main>
  <div class="abs panel"></div>

  <section>
    <div class="abs hero" role="img" aria-label="Hockey stick blade resting on a puck on dark ice"></div>
    <h1 class="abs hero-title heading">INTEGER ULTRICIES</h1>
    <p class="abs hero-text">Donec ullamcorper tristique sagittis. In laoreet eget urna eu pulvinar. Donec vel massa varius massa semper gravida ac nec diam. Duis in pellentesque tellus. Donec eget orci orci. Pellentesque faucibus sem non vulputate euismod.</p>
    <div class="abs slide-num active" style="top:220px">1</div>
    <div class="abs slide-num" style="top:250px">2</div>
    <div class="abs slide-num" style="top:280px">3</div>
  </section>

  <!-- article one -->
  <article>
    <div class="abs card" style="left:167px;top:327px;width:374px;height:234px"></div>
    <div class="abs photo" style="left:169px;top:330px;width:170px;height:152px;background:linear-gradient(#3a3f49,#b9bec7 70%,#e4e6ea)" role="img" aria-label="Goalie in full gear crouched in front of the net"></div>
    <div class="abs card-body" style="left:340px;top:330px;width:168px;height:152px"></div>
    <div class="abs label" style="left:145px;top:341px">Vitae Odio</div>
    <h2 class="abs card-title heading" style="left:348px;top:338px">Fusce sodales rhoncus</h2>
    <p class="abs" style="left:348px;top:361px;width:156px;font-size:8px">Nulla purus risus, sagittis ac tristique a, cursus sed eros. In accumsan vulputate arcu, id luctus arcu aliquam in</p>
    <ul class="abs bullets" style="left:350px;top:404px;width:156px;font-size:8px">
      <li><b>Auris Consectetur Cursus</b><br>Curabitur sed aliquet ut a vestibulum molestie</li>
      <li><b>Nullam nisl eros</b><br>laoreet hendrerit lacus. Donec mattis ultricies nulla bibendum iaculis.</li>
    </ul>
    <div class="abs share">SHARE<i></i><i></i><i></i></div>
    <div class="abs dot-list" style="left:183px;top:498px">
      <span>Aliquam molestie nisi sed tellus.</span><span>Sed ut nulla vitae felis consectetur.</span>
      <span>Sed dapibus ante viverra.</span><span>Donec ac tortor est.</span>
      <span>Aenean tellus purus, dapibus eget.</span><span>Mauris eget leo scelerisque, tortor id.</span>
    </div>
  </article>

  <!-- article two -->
  <article>
    <div class="abs card" style="left:167px;top:574px;width:374px;height:154px"></div>
    <div class="abs photo" style="left:169px;top:576px;width:168px;height:150px;background:linear-gradient(#d9dde3,#f3f4f6)" role="img" aria-label="Skater's legs and stick handling a puck on ice"></div>
    <div class="abs card-body" style="left:338px;top:576px;width:201px;height:150px"></div>
    <div class="abs label" style="left:145px;top:585px">Lorem Ipsum</div>
    <h2 class="abs card-title heading" style="left:348px;top:583px">Lorem ipsum dolor sit amet</h2>
    <p class="abs" style="left:348px;top:605px;width:184px;font-size:8px">Lorem ipsum dolor sit amet, consectetur adipiscing elit. Donec posuere eros in ipsum viverra, sed rutrum eros tempus. Proin nec fermentum odio. Duis vulputate libero in urna commodo, sit amet tincidunt leo varius. Nam eget dictum est. Aliquam convallis odio eu erat mollis adipiscing.</p>
    <div class="abs btn" style="left:348px;top:702px">MORE INFORMATION</div>
  </article>

  <!-- sidebar -->
  <aside>
    <div class="abs search">
      <h3>SEARCH <b style="font-weight:500">OUR SITE</b></h3>
      <div class="field">Search...</div>
      <div class="opts"><span>local</span><span>web</span><span>images</span></div>
    </div>
    <div class="abs info-box">
      <h3>CURABITUR SED ARCU EU ENIM</h3>
      <p>Fusce feugiat commodo augue, sit amet hendrerit sapien sodales et. Donec lacinia purus eu accumsan posuere.</p>
      <p>Mauris placerat vel sem eget varius. Cras pharetra massa quis commodo tincidunt.</p>
    </div>
    <div class="abs tabs"><span class="active">PHASELLUS</span><span>MAGNA</span></div>
    <div class="abs thumb" style="left:554px;top:600px;width:48px;height:48px" role="img" aria-label="Stick and puck close-up"></div>
    <p class="abs side-text" style="left:612px;top:600px">Phasellus ac leo rhoncus, scelerisque eros nec, elementum eros. Maecenas sollicitudin interdum elit.</p>
    <div class="abs thumb" style="left:554px;top:659px;width:48px;height:48px;background:linear-gradient(#222,#888 50%,#111)" role="img" aria-label="Players on the ice"></div>
    <p class="abs side-text" style="left:612px;top:660px">Curabitur sed arcu eu enim accumsan euismod. Fusce quis nunc egestas, venenatis eros ac, pellentesque risus.</p>
  </aside>

  <div class="abs ticker"><b>Neque porro quisquam est:</b> Donec tempus eros ut ultrices mollis. Sed pellentesque vitae enim in consequat....<div class="arrows"><i></i><i></i></div></div>

  <!-- three columns -->
  <section>
    <h3 class="abs col-head" style="left:178px;top:783px">NULLA SEMPER JUSTO QUIS MAURIS</h3>
    <div class="abs col-bar" style="left:178px;top:800px;width:163px"></div>
    <div class="abs frame" style="left:180px;top:821px;width:160px;height:108px"></div>
    <div class="abs" style="left:186px;top:827px;width:148px;height:96px;background:linear-gradient(#f2f2f2,#c9c9cc)" role="img" aria-label="Hockey equipment laid out"></div>
    <div class="abs caption" style="left:195px;top:877px;width:138px"><b>INTEGER UT TEMPOR SEM</b><br>Aliquam mattis, libero eu sagittis</div>

    <h3 class="abs col-head" style="left:369px;top:783px">DUIS SIT AMET FRINGILLA EST</h3>
    <div class="abs col-bar" style="left:369px;top:800px;width:162px"></div>
    <div class="abs frame" style="left:371px;top:821px;width:48px;height:48px;background:#6b5a2c" role="img" aria-label="Gear thumbnail"></div>
    <div class="abs frame" style="left:426px;top:821px;width:48px;height:48px;background:#a9c0d8" role="img" aria-label="Net thumbnail"></div>
    <div class="abs frame" style="left:482px;top:821px;width:48px;height:48px;background:#e6d8d8" role="img" aria-label="Sticks thumbnail"></div>
    <div class="abs frame" style="left:371px;top:880px;width:48px;height:48px;background:#5d5130" role="img" aria-label="Gear thumbnail"></div>
    <div class="abs frame" style="left:426px;top:880px;width:48px;height:48px;background:#d8d9dc" role="img" aria-label="Skates thumbnail"></div>
    <div class="abs frame" style="left:482px;top:880px;width:48px;height:48px;background:#e8d6d8" role="img" aria-label="Pucks thumbnail"></div>

    <h3 class="abs col-head" style="left:560px;top:783px">ELEMENTUM PURUS TORTOR AT MI.</h3>
    <div class="abs col-bar" style="left:560px;top:800px;width:162px"></div>
    <div class="abs slider"><h4>Vestibulum fermentum</h4><p>Duis sit amet fringilla est. Aenean sollicitudin nulla at orci hendrerit tincidunt. In sit amet libero nibh. Phasellus ac dignissim risus, ut imperdiet ligula....</p></div>
    <svg class="abs" style="left:563px;top:921px" width="160" height="9" viewBox="0 0 160 9">
      <circle cx="3" cy="4" r="2.3" fill="#4a7ab8"/><circle cx="9" cy="4" r="2.3" fill="#555"/><circle cx="15" cy="4" r="2.3" fill="#555"/>
      <circle cx="144" cy="4.5" r="4.5" fill="#333"/><circle cx="155" cy="4.5" r="4.5" fill="#333"/>
      <path d="M145.5 2.5 143 4.5 145.5 6.5M153.5 2.5 156 4.5 153.5 6.5" stroke="#fff" fill="none"/>
    </svg>
  </section>
</main>

<footer>
  <div class="abs footer"></div>
  <h3 class="abs f-head" style="left:176px;top:980px">MAECENAS ET URNA IN URNA</h3>
  <div class="abs col-bar" style="left:176px;top:997px;width:163px"></div>
  <ul class="abs f-list" style="left:176px;top:1013px;width:160px">
    <li><b>Aenean dictum</b>In malesuada elit. Vestibulum non volutpat tellus. Curabitur pretium leo fringilla purus lobortis auctor.</li>
    <li><b>Maecenas quis elit mollis</b>Suspendisse potenti. Pellentesque porttitor et diam at lobortis. Sed lacus est, condimentum</li>
    <li><b>Quisque pulvinar tellus metus</b>Morbi dictum quam dapibus tristique.</li>
  </ul>

  <h3 class="abs f-head" style="left:367px;top:980px">QUISQUE FAUCIBUS MASSA SIT AMET</h3>
  <div class="abs col-bar" style="left:367px;top:997px;width:163px"></div>
  <p class="abs f-text" style="left:367px;top:1014px;width:162px">Donec mollis sed orci placerat iaculis. Ut venenatis turpis eu fringilla pretium. Praesent suscipit mi fringilla iaculis porttitor. Vestibulum varius a tortor at rutrum.</p>
  <p class="abs f-text" style="left:367px;top:1072px;width:162px">Suspendisse ullamcorper malesuada mi, nec facilisis ante luctus at. In urna ligula, suscipit quis enim sed, congue aliquet elit. Suspendisse in odio mattis, turpis. Aliquam elementum dui cursus orci adipiscing</p>

  <h3 class="abs f-head" style="left:558px;top:980px">CONTACT <b style="font-weight:500">DETAILS</b></h3>
  <div class="abs col-bar" style="left:558px;top:997px;width:163px"></div>
  <div class="abs contact-row" style="left:568px;top:1014px">
    <svg width="16" height="12" viewBox="0 0 16 12"><path d="M1 4Q8-1 15 4L13 6 11 4H5L3 6ZM4 6H12L14 11H2Z" fill="#333"/></svg>
    <span><a>+1 (555) 555-555-5555</a><br><a>+1 (555) 555-555-5556</a></span>
  </div>
  <div class="abs contact-row" style="left:570px;top:1050px">
    <svg width="12" height="14" viewBox="0 0 12 14"><path d="M6 0A5 5 0 0 1 11 5C11 9 6 14 6 14S1 9 1 5A5 5 0 0 1 6 0Z" fill="#333"/><circle cx="6" cy="5" r="2" fill="#c8ccd2"/></svg>
    <span>Ut venenatis turpis<br>Donec mollis sed orci<br>Seattle, WA 00000, USA</span>
  </div>
  <div class="abs contact-row" style="left:568px;top:1103px">
    <svg width="16" height="11" viewBox="0 0 16 11"><rect width="16" height="11" fill="#333"/><path d="M0 0 8 6 16 0" stroke="#c8ccd2" fill="none"/></svg>
    <span>noreply@domain.com</span>
  </div>
  <div class="abs footer-bottom"></div>
  <div class="abs to-top"></div>
</footer>

</body>
</html>
```